VRL Gel Nail Polish Collection for 15 ml bottle

We need a design for our new collection of VRL brand gel nail polish, called "SILK DUSK". We are a nail salon / beauty supply distributor selling to retail nail salons in the US. Please look at the sample nail polish bottles attached for your reference. Our bottle will be white with a silver cap. Also, please look at our other project that is on PX for label design for the matching color tip swatches.

Target Market(s)

Retail Nail Salons in the US

Industry/Entity Type

Nail Salon

Colors

Designer to choose colors to be used in the design.

Requirements
Must have
• VRL logo - this needs to be changed to black color for letters VRL and matte gold for the "drop".
• PREMIUM GEL POLISH, SILK DUSK, 0.5 oz (15 ml), back label wording.
• Front label wording must be clear and easy to read.
• Dimensions of label must be 1.125" x 4.0".
• Front part of label and back part of label must be spaced correctly so that they will be on opposite sides of the bottle.
Nice to have
• Color stripe possibly where the product name "SILK DUSK" will appear, so that it stands out.
Should not have
• no actual pictures of SILK DUSK, no overpowering graphics

```html
<!DOCTYPE html>
<html lang="en">
<head>
<meta charset="utf-8">
<title>VRL Premium Gel Polish – Silk Dusk Label</title>
<link rel="stylesheet" href="https://fonts.googleapis.com/css2?family=Marcellus&display=swap">
<style>
  :root {
    --canvas: #f3f3f3;
    --label-white: #ffffff;
    --ink: #111111;
    --gold-dark: #8a5a1c;
    --gold-mid: #b88a3c;
    --gold-light: #f1d48a;
    --gold-text: #a8742a;
    --silver-dark: #8e8e8e;
    --silver-light: #f7f7f7;
  }
  * { box-sizing: border-box; margin: 0; padding: 0; }
  html, body {
    width: 1200px;
    height: 960px;
    overflow: hidden;
    background: var(--canvas);
  }
  .label {
    position: absolute;
    left: 237px;
    top: 70px;
    width: 725px;
    height: 820px;
    background: var(--label-white);
    box-shadow: 0 1px 4px rgba(0,0,0,0.18);
    font-family: "Marcellus", "Optima", serif;
  }
  .label__bands {
    position: absolute;
    inset: 0;
    width: 100%;
    height: 100%;
  }
  .label__content {
    position: absolute;
    inset: 0;
    display: flex;
    flex-direction: column;
    align-items: center;
  }
  .brand {
    margin-top: 150px;
    display: flex;
    align-items: center;
    gap: 14px;
  }
  .brand__name {
    font-size: 150px;
    line-height: 1;
    color: var(--ink);
    letter-spacing: -2px;
  }
  .brand__drop {
    width: 34px;
    height: 34px;
    border-radius: 50%;
    background: var(--gold-mid);
    align-self: flex-start;
    margin-top: 12px;
  }
  .product-line {
    margin-top: 44px;
    text-align: center;
  }
  .product-line__premium {
    font-size: 52px;
    line-height: 1;
    color: var(--gold-text);
    letter-spacing: 2px;
  }
  .product-line__type {
    margin-top: 6px;
    font-size: 60px;
    line-height: 1;
    color: var(--ink);
    letter-spacing: 4px;
    padding-bottom: 10px;
    border-bottom: 3px solid var(--gold-mid);
  }
  .shade {
    margin-top: 46px;
    width: 430px;
    height: 134px;
    border-radius: 67px;
    background: linear-gradient(90deg, var(--gold-dark) 0%, var(--gold-light) 22%, var(--gold-mid) 55%, var(--gold-dark) 100%);
    box-shadow: inset 0 0 0 4px rgba(241,212,138,0.8);
    display: flex;
    align-items: center;
    justify-content: center;
  }
  .shade__name {
    font-size: 66px;
    line-height: 1;
    color: #ffffff;
    letter-spacing: 1px;
  }
</style>
</head>
<body>
  <div class="label">
    <svg class="label__bands" viewBox="0 0 403 455" preserveAspectRatio="none" aria-hidden="true">
      <defs>
        <linearGradient id="silver-band" x1="0" y1="0" x2="0" y2="1">
          <stop offset="0" stop-color="#a9a9a9"/>
          <stop offset="0.3" stop-color="#e9e9e9"/>
          <stop offset="0.5" stop-color="#ffffff"/>
          <stop offset="0.7" stop-color="#9a9a9a"/>
          <stop offset="1" stop-color="#d9d9d9"/>
        </linearGradient>
      </defs>
      <path class="band band--left" d="M0 0 L14 0 Q62 227 14 455 L0 455 Z" fill="url(#silver-band)"/>
      <path class="band band--right" d="M403 0 L389 0 Q341 227 389 455 L403 455 Z" fill="url(#silver-band)"/>
    </svg>
    <div class="label__content">
      <div class="brand">
        <span class="brand__name">VRL</span>
        <span class="brand__drop"></span>
      </div>
      <div class="product-line">
        <p class="product-line__premium">PREMIUM</p>
        <p class="product-line__type">GEL POLISH</p>
      </div>
      <div class="shade">
        <span class="shade__name">SILK DUSK</span>
      </div>
    </div>
  </div>
</body>
</html>
```